Broschüre in Querformat für Immobilienmakler
Zielgruppe
Immobilienmakler - Überregional tätig - zielgerichtete Vermarktung - Zielgruppe sind Verkäufer oft ältere Menschen
Ich möchte eine Broschüre mit 12 Seiten im Querformat - Die Broschüre sollte der Website morvatin-immobilien.de ein wenig ähneln.
Aufgabenstellung
klare Linie - schnell erklärbar und übersichtlich - logischer Aufbau - Aufmerksamkeit erwecken durch Bilder - schnelle Info für Querleser - VERTRAUEN - ehrlich und authentisch - nicht Eitel - schnelle Zurechtfindung - Serviceorientiert - Rundumsorglos Paket

```html
<!DOCTYPE html>
<html lang="de">
<head>
<meta charset="utf-8">
<title>Morvatin Immobilien – Broschüre</title>
<link href="https://fonts.googleapis.com/css2?family=Montserrat:wght@400;600;700&family=Open+Sans:wght@400;600;700&display=swap" rel="stylesheet">
<style>
:root{
  --stage:#ececec;
  --page:#ffffff;
  --page-grey:#e9e9eb;
  --blue:#2f7fb1;
  --blue-dark:#1f5a87;
  --blue-light:#5fa3cf;
  --ink:#2b2b2b;
  --muted:#6b6b6b;
  --row:#dcdcdc;
  --green:#4caf50;
  --yellow:#e8c53a;
  --red:#d23a3a;
}
*{box-sizing:border-box;margin:0;padding:0}
html,body{width:1200px;height:3973px;overflow:hidden}
body{background:var(--stage);font-family:"Open Sans",sans-serif;color:var(--ink);position:relative}
.spread{position:absolute;left:160px;width:880px;height:325px;display:flex;box-shadow:0 6px 14px rgba(0,0,0,.12)}
.page{position:relative;width:440px;height:325px;background:var(--page);overflow:hidden}
.page + .page{border-left:1px solid #d8d8d8}
.abs{position:absolute}
.h{font-family:"Montserrat",sans-serif;font-weight:700}
.t{font-size:5.2px;line-height:1.55;color:var(--muted)}
.t p{margin-bottom:3px}
.white{color:#fff}
.blue{color:var(--blue)}
.photo{position:absolute}
.brand{font-family:"Montserrat",sans-serif;font-weight:600;font-size:13px;color:var(--blue-dark);white-space:nowrap}
.brand.light{color:#fff}
.rows div{display:flex;justify-content:space-between;height:11px;align-items:center;padding:0 5px;font-size:5px;font-weight:700;font-family:"Montserrat",sans-serif}
.rows div:nth-child(odd){background:var(--row)}
.bullets li{list-style:none;position:relative;padding-left:8px;margin-bottom:4px;font-size:5px;line-height:1.5;color:var(--muted)}
.bullets li::before{content:"";position:absolute;left:0;top:2px;width:3px;height:3px;border-radius:50%;background:var(--blue)}
.info{width:100%;border-collapse:collapse;font-size:4.8px;color:#fff}
.info td{padding:1.4px 3px}
.info td.c{text-align:center;width:28px}
.tick{color:#8fe28f}
.box{position:absolute;border:1px solid var(--blue);background:#fff;font-size:5px}
.box .bh{background:var(--blue);color:#fff;font-weight:700;padding:3px 6px;font-size:5.2px}
.box .br{display:flex;justify-content:space-between;padding:1.5px 6px;color:var(--ink)}
</style>
</head>
<body>

<!-- Spread 1: cover -->
<section class="spread" style="top:224px">
  <div class="page" style="background:var(--page-grey)">
    <div class="brand abs" style="left:22px;top:44px">Morvatin Immobilien</div>
    <div class="abs t" style="left:22px;top:260px;line-height:1.7">Montag - Freitag<br>09:00 Uhr bis 18:00 Uhr<br>Samstag und Sonntag<br>nach Vereinbarung</div>
    <div class="abs" style="right:12px;top:240px;text-align:right">
      <div class="h blue" style="font-size:13px;margin-bottom:4px">Morvatin Immobilien</div>
      <div class="t" style="line-height:1.75">Lindenhofer Str. 12<br>D-49001 Talbruck<br>Telefon: +49 (0)4471 000 123<br>jonas@morvatin-immobilien.de<br><b style="color:var(--ink)">www.morvatin-immobilien.de</b></div>
    </div>
  </div>
  <div class="page">
    <div class="photo" role="img" aria-label="Foto eines modernen Wohnhauses mit blauer Farbüberlagerung" style="inset:0;background:linear-gradient(160deg,#3b8cc2 0%,#2a6fa3 55%,#1f5a87 100%)"></div>
    <div class="abs" style="left:20px;top:18px;right:12px;bottom:20px;border:2px solid #fff"></div>
    <div class="brand light abs" style="right:40px;top:70px">Morvatin Immobilien</div>
    <div class="abs h white" style="left:28px;top:252px;font-size:12.5px;line-height:1.6;font-weight:600">Immobilien, Häuser &amp; Wohnungen<br>schnell suchen und finden!</div>
  </div>
</section>

<!-- Spread 2: about -->
<section class="spread" style="top:891px">
  <div class="page">
    <div class="photo" role="img" aria-label="Graues Foto eines Bürohochhauses" style="left:0;top:0;width:140px;height:200px;background:linear-gradient(180deg,#d7d7d9,#9a9ca0)"></div>
    <div class="photo" role="img" aria-label="Porträtfoto des Inhabers" style="left:65px;top:35px;width:60px;height:62px;background:linear-gradient(180deg,#cfd2d6,#7e858d)"></div>
    <div class="abs h blue" style="left:140px;top:36px;font-size:9px">Jonas Morvatin</div>
    <div class="abs t" style="left:140px;top:47px;font-size:4.3px">kein Chef, sondern der Kleber, der das Team zusammenhält</div>
    <div class="abs t" style="left:140px;top:58px;width:280px">
      <p>Wir kämpfen jeden Tag gegen das schlechte Image der Branche. Nicht zu Unrecht, wie meine Berufserfahrung bei großen Maklerunternehmen gezeigt hat. Für mich stand schnell fest:</p>
      <p>Ein eigenes Maklerbüro muss her. Seitdem kann ich endlich auch ohne Zeitdruck arbeiten. Ein guter Eindruck darf bei uns ausschließlich durch Kompetenz, Transparenz, aber vor allem durch Zeit und einen sympathischen Umgang hinterlassen werden.</p>
      <p>Und die Rechnung geht auf: Wir wachsen stetig und haben mittlerweile mehrere Mitarbeiter beschäftigt, ändern die innere Haltung zur kundenorientierten Vermittlung aber nicht.</p>
    </div>
    <div class="abs" style="left:20px;right:0;top:185px;height:115px;background:var(--blue)">
      <div class="h white" style="position:absolute;left:10px;top:10px;font-size:9px">Die Firmengeschichte</div>
      <div class="t white" style="position:absolute;left:10px;top:26px;right:12px;font-size:5.6px;line-height:1.65">Jonas Morvatin, gelernter Bankkaufmann und Firmeninhaber von Morvatin Immobilien, ist seit vielen Jahren im Bereich der Immobilienvermittlung tätig. Ob Verkauf oder Vermietung, einzigartig ist der Rundumservice (mehr Informationen: Rundumservice). Inzwischen ist das Team auf vier Mitarbeiter mit unterschiedlichen Fachgebieten und Sprachkenntnissen angewachsen. So können selbst die ungewöhnlichsten Aufgaben schnell und professionell im Unternehmen bewältigt werden.</div>
    </div>
  </div>
  <div class="page">
    <div class="abs h" style="left:20px;top:35px;font-size:8px;line-height:1.5">Warum sollten Sie sich für Uns,<br>kleine <span class="blue">Makler entscheiden?</span></div>
    <div class="abs t" style="left:20px;top:64px;right:20px">Hohes Engagement, gepaart mit nachweislichen Erfahrungswerten, ein starkes Netzwerk und Vertrauensbasis zeichnen den perfekten Makler aus. Wenn der Chef selbst aktiv ist, werden auch Extra-Meilen gemacht, um eine Zufriedenheit von Käufer und Verkäufer sicherzustellen und eine hohe Umsetzungsgeschwindigkeit zu garantieren. Eine persönliche Bindung sowie durchgehende Erreichbarkeit ist aufgrund der flachen Hierarchie stets gegeben. Abstimmungsprozesse über Hierarchieebenen sind uns fremd, während ein Großunternehmen Datenbanken befüllt, Meetings besucht und Fahrkosten abrechnet. Urlaub plant und Exposés diskutiert, sind wir bereits am Besichtigen.</div>
    <div class="abs" style="left:0;right:0;top:170px;height:130px;background:var(--blue)"></div>
    <div class="abs" style="left:40px;right:40px;top:145px;height:82px;background:#fff;box-shadow:0 2px 6px rgba(0,0,0,.15);text-align:center;padding:10px 14px">
      <div class="h" style="font-size:7.5px">Der sicherste Weg zum <span class="blue">erfolgreichen Immobilienverkauf</span></div>
      <div class="t" style="font-size:4.2px;margin-bottom:6px">Vertrauen Sie auf unsere Erfahrung</div>
      <div class="t">Wer eine Immobilie im Alleingang verkauft, braucht viel Zeit, Nerven und Geld. Erst bezüglich marktgerechter Schauläufe ihres privaten Raumes, dann wird versucht den Preis massiv zu drücken, und zum Schluss platzen Finanzierungen. Mit dem Rundumservice bleibt Ihnen dieser Ärger erspart.</div>
    </div>
  </div>
</section>

<!-- Spread 3: schedule & team -->
<section class="spread" style="top:1519px">
  <div class="page">
    <div class="abs" style="left:262px;top:0;width:178px;height:100%;background:var(--blue)"></div>
    <div class="abs h blue" style="left:52px;top:64px;font-size:7px">Leistung</div>
    <div class="abs h blue" style="left:182px;top:52px;font-size:7px;line-height:1.4">Zeitplan der<br>Ausführung</div>
    <div class="abs rows" style="left:24px;top:88px;width:238px">
      <div><span>Wertermittlung</span><span>maximal 3 Werktage</span></div>
      <div><span>Marktanalyse</span><span>maximal 3 Werktage</span></div>
      <div><span>Erstellung des professionellen Exposés</span><span>3 Werktage</span></div>
      <div><span>Erstellung professioneller Grundrisse</span><span>2 Werktage</span></div>
      <div><span>Nachbearbeitung Fotos</span><span>3 Werktage</span></div>
      <div><span>Vermarktungsbeginn Internet</span><span>3 Werktage</span></div>
      <div><span>Info an vorgemerkte Interessenten</span><span>5 Werktage</span></div>
      <div><span>Erreichbarkeit</span><span>täglich</span></div>
      <div><span>Finanzierungsangebote</span><span>12 Werktage maximal</span></div>
      <div><span>Veröffentlichung Homepage</span><span>3 Werktage</span></div>
      <div><span>360 Tour erstellen</span><span>5 Werktage</span></div>
      <div><span>Erstellung Energieausweis</span><span>2 Werktage</span></div>
    </div>
    <div class="abs t white" style="left:272px;top:160px;width:122px;font-size:4.8px">
      <p><b>Situationsbedingt sind weitere Leistungen nicht ausgeschlossen</b></p>
      <p><b>Wichtig für Sie:</b> Der aktuelle Markt legt letztendlich den Kaufpreis fest (Angebot und Nachfrage). Eine professionelle und breit gestreute Vermarktung ist hier von wichtiger Bedeutung. Aus eigener praxisorientierter Erfahrung können wir Ihnen bestätigen, dass Sie durch ihre Nachbarschaft oder Freundeskreis keine Information über Marktpreise erhalten, eher spielt die Neugier eine größere Rolle.</p>
    </div>
  </div>
  <div class="page">
    <div class="abs" style="left:0;right:0;top:18px;text-align:center;font-family:Montserrat,sans-serif;font-size:17px;color:var(--ink)">Our <span class="blue" style="font-weight:600">Teams</span></div>
    <div class="photo" role="img" aria-label="Porträtfoto eines Mitarbeiters" style="left:20px;top:60px;width:52px;height:56px;background:linear-gradient(180deg,#e4e4e6,#8d929a)"></div>
    <div class="abs" style="left:78px;top:72px">
      <div class="h blue" style="font-size:7px">Deniz Arslan</div>
      <div class="t" style="font-size:4.5px">deniz@morvatin-immobilien.de<br>tel.: (04471) 000 12 40</div>
    </div>
    <div class="photo" role="img" aria-label="Porträtfoto einer Mitarbeiterin" style="left:222px;top:60px;width:52px;height:56px;background:linear-gradient(180deg,#e4e4e6,#8d929a)"></div>
    <div class="abs" style="left:316px;top:72px">
      <div class="h blue" style="font-size:7px">Lena Hausig</div>
      <div class="t" style="font-size:4.5px">lena@morvatin-immobilien.de<br>tel.: (04471) 000 12 41</div>
    </div>
    <div class="photo" role="img" aria-label="Grauer Hintergrund mit Stadtsilhouette" style="left:20px;top:140px;width:420px;height:185px;background:linear-gradient(180deg,#ffffff 0%,#f1f2f4 45%,#c9ccd0 100%)"></div>
    <div class="photo" role="img" aria-label="Foto zweier Mitarbeiter mit verschränkten Armen" style="left:40px;top:150px;width:110px;height:175px;background:linear-gradient(180deg,#dfe3e8,#7f8a97)"></div>
    <div class="abs" style="left:240px;top:158px">
      <div class="h blue" style="font-size:7px">Jonas Morvatin</div>
      <div class="t" style="font-size:4.5px">jonas@morvatin-immobilien.de<br>tel.: (04471) 000 12 42</div>
    </div>
    <div class="abs" style="left:300px;top:212px">
      <div class="h blue" style="font-size:7px">Carla Wendt</div>
      <div class="t" style="font-size:4.5px">carla@morvatin-immobilien.de<br>tel.: (0176) 000 33 19</div>
    </div>
  </div>
</section>

<!-- Spread 4: services & principles -->
<section class="spread" style="top:2143px">
  <div class="page">
    <div class="photo" role="img" aria-label="Graues Foto einer Bürofassade" style="left:170px;top:0;width:270px;height:300px;background:linear-gradient(180deg,#f0f0f0,#b9bbbe 70%,#6f7276)"></div>
    <div class="abs" style="left:0;right:0;top:270px;height:16px;background:var(--blue-light)"></div>
    <div class="abs h" style="left:22px;top:24px;font-size:8.5px;line-height:1.5">UNSERE LEISTUNGEN<br>FÜR <span class="blue">IMMOBILIENVERKÄUFER</span></div>
    <div class="abs" style="left:18px;top:56px;width:320px;height:208px;background:#fff"></div>
    <ul class="abs bullets" style="left:22px;top:62px;width:130px">
      <li>Realistische Wertermittlung, basierend auf Marktanalyse und vergleichbaren Angeboten</li>
      <li>Zielgruppenanalyse zur Ermittlung passender Käufer</li>
      <li>Stärken-/Schwächen-Analyse zur optimalen Aufbereitung und Präsentation der Immobilie</li>
      <li>Professionelle Exposéerstellung mit aussagekräftigen Fotos, Texten und Grundrissplänen</li>
      <li>Vermarktung in Internetportalen, auf unserer Homepage, in Printmedien</li>
      <li>Open House Veranstaltungen (offene Hausbesichtigungen)</li>
      <li>Durchführung von Gemeinschaftsgeschäften mit Maklerkollegen aus unserem deutschlandweiten Netzwerk</li>
    </ul>
    <ul class="abs bullets" style="left:170px;top:62px;width:150px">
      <li>Besichtigungen nur mit geprüften Interessenten</li>
      <li>Bonitätsprüfung von Kaufinteressenten</li>
      <li>Vorbereitung des Notarvertrages sowie Begleitung und Betreuung beim Notartermin</li>
      <li>Bankenunabhängige Finanzierungsberatung und Übernahme der gesamten Abwicklung</li>
      <li>Professionelle Preisverhandlungen für maximalen Kaufpreis</li>
      <li>After Sales Service</li>
    </ul>
  </div>
  <div class="page">
    <div class="abs" style="left:0;top:0;width:52px;height:100%;background:var(--blue)"></div>
    <div class="abs" style="right:12px;top:0;width:3px;height:100%;background:var(--blue)"></div>
    <div class="abs white" style="left:28px;top:160px;transform:translate(-50%,-50%) rotate(-90deg);white-space:nowrap;text-align:center">
      <div class="h" style="font-size:10px">Unternehmerische Grundsätze</div>
      <div style="font-size:4.2px;letter-spacing:.4px">WERTE, DIE UNSERE ARBEIT JEDEN TAG TRAGEN</div>
    </div>
    <div class="abs t" style="left:66px;top:18px;right:24px">
      <div class="h blue" style="font-size:5.5px">EHRLICHKEIT</div>
      <p>Wir wissen, dass dauerhafte Beziehungen im privaten wie auch geschäftlichen Bereich nur auf einer Basis bestehen können, bei der man ehrlich miteinander umgeht. Zur Ehrlichkeit gehört auch, Unbequemes offen anzusprechen und Mängel nicht zu verschweigen.</p>
      <div class="h blue" style="font-size:5.5px;margin-top:6px">VERANTWORTUNG</div>
      <p>Bei Immobiliengeschäften geht es häufig um sehr viel Geld und für das weitere Leben wichtige Entscheidungen. Wir sind uns dieser Bedeutung voll bewusst und übernehmen im Rahmen unseres Einflussbereiches Verantwortung.</p>
      <div class="h blue" style="font-size:5.5px;margin-top:6px">KOMPETENZ</div>
      <p>Kompetenz bedeutet Fachwissen, die Fähigkeit dieses verständlich zu kommunizieren und dementsprechend zu handeln. Um unsere Kompetenz fortlaufend weiter auszubauen, wird in die Weiterentwicklung unserer Mitarbeiter investiert.</p>
      <div class="h blue" style="font-size:5.5px;margin-top:6px">FAIRNESS</div>
      <p>Wir gehen offen und ehrlich mit allen Beteiligten um und sorgen dafür, dass bei Entscheidungen alle wichtigen Punkte berücksichtigt werden.</p>
      <div class="h blue" style="font-size:5.5px;margin-top:6px">ERFOLG</div>
      <p>Wir sind der Meinung, gute Leistung bewirkt und verdient Anerkennung. Wir haben uns zu einer herausragenden Leistung verpflichtet und sind stolz auf den erzielten Erfolg, der sich in der Anerkennung unserer Kunden zeigt.</p>
    </div>
  </div>
</section>

<!-- Spread 5: info sheet & FAQ -->
<section class="spread" style="top:2783px">
  <div class="page">
    <div class="photo" role="img" aria-label="Foto eines Gebäudes mit dunkelblauer Farbüberlagerung" style="inset:0;background:linear-gradient(170deg,#3a86b8,#1f5a87 60%,#173f60)"></div>
    <div class="abs h white" style="left:22px;top:22px;font-size:10px">INFOBLATT</div>
    <div class="abs h" style="left:282px;top:14px;width:28px;height:26px;background:var(--green);color:#fff;font-size:5.5px;display:flex;align-items:center;justify-content:center">WIR</div>
    <div class="abs h" style="left:310px;top:10px;width:28px;height:30px;background:var(--yellow);color:#fff;font-size:5.5px;display:flex;align-items:center;justify-content:center;text-align:center">Sie<br>selbst</div>
    <div class="abs h white" style="left:338px;top:12px;width:28px;height:28px;font-size:5.5px;display:flex;align-items:center;justify-content:center;text-align:center">Makler<br>XY</div>
    <table class="abs info" style="left:50px;top:46px;width:316px">
      <tr><td>Regelmäßige Teilnahme an Fort-/Weiterbildungsmaßnahmen</td><td class="c tick">✓</td><td class="c">?</td><td class="c">?</td></tr>
      <tr><td>Hauptberufliche Tätigkeit mit Erlaubnis nach §34c GewO</td><td class="c tick">✓</td><td class="c">?</td><td class="c">?</td></tr>
      <tr><td>Telefonische Erreichbarkeit - an 365 Tagen von 24/7</td><td class="c tick">✓</td><td class="c">?</td><td class="c">?</td></tr>
      <tr><td>Professionelle Objektfotografie / eigener Profi-Fotograf</td><td class="c tick">✓</td><td class="c">?</td><td class="c">?</td></tr>
      <tr><td>Virtuelle 360° - Immobilienbesichtigungen</td><td class="c tick">✓</td><td class="c">?</td><td class="c">?</td></tr>
      <tr><td>Individuelle Farbexposés für jeden Verkaufs-Angebot</td><td class="c tick">✓</td><td class="c">?</td><td class="c">?</td></tr>
      <tr><td>Werbemaßnahmen direkt an Objekt (nach Absprache)</td><td class="c tick">✓</td><td class="c">?</td><td class="c">?</td></tr>
      <tr><td>Regionale Marktkenntnis</td><td class="c tick">✓</td><td class="c">?</td><td class="c">?</td></tr>
      <tr><td>Kostenfreie Marktwertanalyse</td><td class="c tick">✓</td><td class="c">?</td><td class="c">?</td></tr>
      <tr><td>Unternehmensbroschüre mit Leistungsverzeichnis</td><td class="c tick">✓</td><td class="c">?</td><td class="c">?</td></tr>
      <tr><td>Termine auch abends, an Wochenenden und Feiertagen</td><td class="c tick">✓</td><td class="c">?</td><td class="c">?</td></tr>
      <tr><td>Erstbesichtigungstermine (keine Massenbesichtigungen)</td><td class="c tick">✓</td><td class="c">?</td><td class="c">?</td></tr>
      <tr><td>Aktuelle Interessentenkartei</td><td class="c tick">✓</td><td class="c">?</td><td class="c">?</td></tr>
      <tr><td>Zahlreiche Referenzobjekte</td><td class="c tick">✓</td><td class="c">?</td><td class="c">?</td></tr>
      <tr><td>Professioneller Internetauftritt</td><td class="c tick">✓</td><td class="c">?</td><td class="c">?</td></tr>
      <tr><td>Erstellung/Beschaffung des Energieausweises</td><td class="c tick">✓</td><td class="c">?</td><td class="c">?</td></tr>
      <tr><td>Prozessoptimierte Arbeit mit spezieller Maklersoftware</td><td class="c tick">✓</td><td class="c">?</td><td class="c">?</td></tr>
      <tr><td>Zusammenarbeit mit unabhängigen Finanzierungsspezialisten</td><td class="c tick">✓</td><td class="c">?</td><td class="c">?</td></tr>
      <tr><td>Gemeinschaftsgeschäfte mit anderen Maklern</td><td class="c tick">✓</td><td class="c">?</td><td class="c">?</td></tr>
      <tr><td>Vermögensschadenhaftpflicht-Versicherung</td><td class="c tick">✓</td><td class="c">?</td><td class="c">?</td></tr>
    </table>
  </div>
  <div class="page">
    <div class="abs t" style="left:14px;top:16px;width:196px;font-size:4.4px">
      <div class="blue" style="font-size:6px;font-weight:600">Ist ein Makler sein Geld wert?</div>
      <p>Wer bei jeder Dienstleistung die Ersparnis sucht, übersieht oft den Wert der Arbeit. Ein Makler übernimmt Bewertung, Vermarktung und Verhandlung und schützt Sie so vor teuren Fehlern beim Verkauf.</p>
      <div class="blue" style="font-size:6px;font-weight:600">Warum erzielt ein Makler einen höheren Verkaufspreis und ist schneller?</div>
      <p>Eine größere Reichweite ist mehr Interessenten, daraus folgen bessere Angebote. 1. Durch die Vermarktung in vielen Kanälen entsteht Nachfrage. 2. Ein Profi kennt den Markt und setzt den richtigen Startpreis. 3. Vorgemerkte Käufer werden sofort informiert.</p>
      <p>Bewertung der Unterlagen, Erstellung des Exposés und Beantwortung der Anfragen erfordern Erfahrung und Zeit, die privaten Verkäufern meist fehlt.</p>
      <div class="blue" style="font-size:6px;font-weight:600">Warum macht der Makler (meistens) die bessere Werbung?</div>
      <p>1. Er hat die technischen Möglichkeiten, virtuelle Rundgänge zu erstellen. 2. Er hat die richtigen Grundrisse der Immobilie. 3. Er hat den Zugang zu allen wichtigen Portalen und nutzt sie gezielt für Ihre Immobilie.</p>
    </div>
    <div class="abs t" style="left:224px;top:16px;width:200px;font-size:4.4px">
      <div class="blue" style="font-size:6px;font-weight:600">Warum sind Sie entspannter und schonen Ihre Nerven (und die Ihrer Familie), wenn Sie einen Makler beauftragen?</div>
      <p>1. Sie ersparen sich unzählige Telefonate und Besichtigungen ohne echtes Kaufinteresse. 2. Sie sind geschützt vor unseriösen Anfragen. 3. Wir kümmern uns um alle Unterlagen. 4. Sie haben einen Fachmann, der Ihre Fragen jederzeit beantwortet.</p>
      <div class="blue" style="font-size:6px;font-weight:600">Warum bevorzugen auch Kaufinteressenten einen Makler?</div>
      <p>1. Sie wissen, dass der Makler ein Fachmann ist und keine wesentlichen Mängel verschweigt. 2. Sie wissen, dass der Makler Ihre Fragen kompetent beantworten kann. 3. Sie erhalten alle Unterlagen vollständig und geordnet.</p>
      <div class="blue" style="font-size:6px;font-weight:600">Makler oder Bank beauftragen?</div>
      <p>1. Die Bank wird den Käufer bevorzugen, der bei ihr finanziert, nicht den, der den höchsten Kaufpreis bietet. 2. Ein unabhängiger Makler vertritt allein Ihre Interessen als Verkäufer und arbeitet für den bestmöglichen Erfolg.</p>
    </div>
  </div>
</section>

<!-- Spread 6: value loss & commission -->
<section class="spread" style="top:3415px">
  <div class="page">
    <div class="brand abs" style="left:22px;top:20px;font-size:11px">Morvatin Immobilien</div>
    <div class="abs h blue" style="right:16px;top:16px;text-align:right;font-size:8px;line-height:1.4;font-weight:600">Angenommener realer<br>Marktwert der Immobilie<br>300.000,-€</div>
    <svg class="abs" style="left:0;top:0" width="440" height="325" viewBox="0 0 440 325" font-family="Open Sans, sans-serif" font-size="5">
      <g fill="none" stroke="#2f7fb1" stroke-width=".8">
        <rect x="65" y="82" width="34" height="11"/><rect x="195" y="82" width="34" height="11"/><rect x="325" y="82" width="34" height="11"/>
        <rect x="36" y="115" width="64" height="15"/><rect x="166" y="115" width="64" height="15"/><rect x="296" y="115" width="64" height="15"/>
      </g>
      <g fill="#2f7fb1" text-anchor="middle">
        <text x="82" y="90">42 Tage</text><text x="212" y="90">281 Tage</text><text x="342" y="90">178 Tage</text>
        <text x="68" y="121">Angebots-Startpreis 315.000,-€</text><text x="198" y="121">Angebots-Startpreis 330.000,-€</text><text x="328" y="121">Angebots-Startpreis 360.000,-€</text>
      </g>
      <g fill="#777" text-anchor="middle" font-size="4">
        <text x="82" y="103">durchschnittliche Vermarktungszeit</text><text x="212" y="103">durchschnittliche Vermarktungszeit</text><text x="342" y="103">durchschnittliche Vermarktungszeit</text>
        <text x="68" y="127">(5% über dem Marktwert)</text><text x="198" y="127">(10% über dem Marktwert)</text><text x="328" y="127">(20% über dem Marktwert)</text>
      </g>
      <g fill="none" stroke="#333" stroke-width=".6"><rect x="72" y="138" width="46" height="11"/><rect x="210" y="142" width="46" height="11"/><rect x="340" y="146" width="46" height="11"/></g>
      <g fill="#333" text-anchor="middle"><text x="95" y="145">Erlös: 297.000,-€</text><text x="233" y="149">Erlös: 289.500,-€</text><text x="363" y="153">Erlös: 255.000,-€</text></g>
      <g fill="#2f7fb1"><rect x="45" y="160" width="22" height="48"/><rect x="175" y="157" width="22" height="51"/><rect x="305" y="151" width="22" height="57"/></g>
      <g fill="#333"><rect x="70" y="164" width="22" height="44"/><rect x="200" y="170" width="22" height="38"/><rect x="330" y="176" width="22" height="32"/></g>
      <line x1="30" y1="208" x2="420" y2="208" stroke="#555" stroke-width=".6"/>
      <g fill="#d23a3a"><rect x="70" y="209" width="22" height="6"/><rect x="200" y="209" width="22" height="12"/><rect x="330" y="209" width="22" height="26"/></g>
      <g fill="#d23a3a" text-anchor="middle" font-weight="700"><text x="81" y="222">- 3.000,-€</text><text x="211" y="228">- 10.500,-€</text><text x="341" y="242">- 45.000,-€</text></g>
      <rect x="45" y="232" width="105" height="20" fill="none" stroke="#d23a3a" stroke-width="1.2"/>
      <text x="97" y="245" text-anchor="middle" fill="#d23a3a" font-family="Montserrat, sans-serif" font-weight="700" font-size="9">Vermögensverlust</text>
    </svg>
  </div>
  <div class="page">
    <div class="box" style="left:30px;top:25px;width:120px">
      <div class="bh">ab 23.12.2020 (alt)</div>
      <div class="br" style="margin-top:4px"><span>Kaufpreis</span><span>100.000,00 €</span></div>
      <div class="br"><span>Käuferprovision 6%</span><span>6.000 €</span></div>
      <div class="br"><span>Grunderwerbsteuer 5%</span><span>5.000 €</span></div>
      <div class="br"><span>Notarkosten 1,5 %</span><span>1.500 €</span></div>
      <div class="bh" style="display:flex;justify-content:space-between;margin-top:6px"><span>Gesamtkosten</span><span>112.500,00 €</span></div>
    </div>
    <div class="abs h white" style="left:256px;top:62px;width:184px;height:28px;background:var(--blue);font-size:10px;display:flex;align-items:center;padding-left:10px">VERKÄUFERPROVISI</div>
    <svg class="abs" style="left:0;top:0" width="440" height="325" viewBox="0 0 440 325">
      <g fill="none" stroke="#2f7fb1" stroke-width="1">
        <path d="M40 105 V260 H170"/><path d="M40 185 H90"/>
        <path d="M250 120 H330 V145"/><path d="M175 145 V140 H250 V120"/>
        <path d="M175 245 V262"/><path d="M335 245 V262"/>
      </g>
      <g fill="#2f7fb1"><path d="M170 257 l6 3 -6 3z"/><path d="M172 262 l3 6 3 -6z"/><path d="M332 262 l3 6 3 -6z"/></g>
      <text x="249" y="205" font-size="14" fill="#2f7fb1" text-anchor="middle">≈</text>
    </svg>
    <div class="box" style="left:110px;top:152px;width:120px">
      <div class="bh" style="text-align:center">Gesetzliche Provisionsteilung</div>
      <div class="br" style="margin-top:4px"><span>Kaufpreis inkl. 3%VK Prov.</span><span>103.000 €</span></div>
      <div class="br"><span>Käuferprovision 3%</span><span>3.090 €</span></div>
      <div class="br"><span>Grunderwerbsteuer 5%</span><span>5.150 €</span></div>
      <div class="br"><span>Notarkosten 1,5 %</span><span>1.545 €</span></div>
      <div class="bh" style="display:flex;justify-content:space-between;margin-top:5px"><span>Gesamtkosten</span><span>112.785 €</span></div>
    </div>
    <div class="box" style="left:268px;top:152px;width:120px">
      <div class="bh" style="text-align:center">Verkäuferprovision</div>
      <div class="br" style="margin-top:4px"><span>Kaufpreis</span><span>106.000 €</span></div>
      <div class="br"><span>Grunderwerbsteuer 5%</span><span>5.300 €</span></div>
      <div class="br"><span>Notarkosten 1,5 %</span><span>1.590 €</span></div>
      <div class="bh" style="display:flex;justify-content:space-between;margin-top:12px"><span>Gesamtkosten</span><span>112.890 €</span></div>
    </div>
    <div class="abs h blue" style="left:152px;top:272px;width:46px;text-align:center;font-size:5.5px">Differenz<br><span style="color:var(--ink);font-weight:400">105.000</span></div>
    <div class="abs h blue" style="left:312px;top:272px;width:46px;text-align:center;font-size:5.5px">Differenz<br><span style="color:var(--ink);font-weight:400">210.000</span></div>
  </div>
</section>

</body>
</html>
```